Counseling Practice Business Card

I need a professional looking business card incorporating my new logo that was just completed. Card needs to incorporate my name and title, description of my specialty, my address, my phone number, my fax number, my email and my website URL. I need to be able to choose design on/with different paper colors and textures.
I do not have a lot of business card ideas so I am open to anything but I want bold,sharp, clear card without additional designs other than my logo (see attached file info). I am open to different color backgrounds or paper colors including black. I do not like traditional brackets around area codes in phone number or dashes between numbers in phone number. Am open to other ways of presenting including periods between numbers as appropriate. I do not know enough to know what I like yet but I want card to coordinate and work together with my logo. My practice emphasizes natural mental health interventions so any use of color (with background paper color or the blue and green in my logo) that elicits nature is nice. In addition to black, any natural brown or wood looking background might be desirable also. Most of the offerings so far look very similar and boring.

Target Market(s)

Potential therapy clients and other professionals

Contact Information for Business Card

Card information:
Marcus T. Whitfield, Ph.D.
Licensed Clinical Psychologist
Integrative Health Coach
4812 Ferndale Pkwy NW
Suite 730
Alder Falls, OR 97412
(541) 555-0142 phone
(541) 555-0186 fax
drmarcuswhitfield@kelvora.com
pathbloomcounseling.com

Font styles to use
Serif
Sans Serif
Other font styles liked:
• anything that you think looks crisp, clear and easily readable

Requirements
Must have
• Any color used should coordinate with my logo design (see attached files).
• Card should be printed horizontally so top and bottom are longest sides of rectangle.
• Background color or paper color should complement and highlight logo. Do not like a white background. black, grey, brown or any color my logo would blend well with.
Nice to have
• I would like designer to utilize color to highlight letters/name or phone-fax-web symbols.
• Bottom edge of card could be highlighted if appropriate to an idea.
Should not have
• I would NOT want the card to have a pure white background at all.
• No clear cards.
• Cards should be oriented with long sides on bottom and top, NOT sides. DO NOT LIKE THIS THIN TALL ORIENTATION.

```html
<!DOCTYPE html>
<html lang="en">
<head>
<meta charset="utf-8">
<title>Pathbloom Counseling – Business Cards</title>
<link rel="stylesheet" href="https://fonts.googleapis.com/css2?family=Tinos:wght@400;700&display=swap">
<style>
  :root {
    --page: #ececec;
    --green: #066a38;
    --blue: #1272bd;
    --ink: #333333;
    --white: #ffffff;
  }
  * { margin: 0; padding: 0; box-sizing: border-box; }
  html, body { width: 960px; height: 1200px; overflow: hidden; }
  body {
    background: var(--page);
    font-family: "Tinos", "Times New Roman", serif;
    position: relative;
  }
  .card {
    position: absolute;
    left: 127px;
    width: 686px;
    height: 390px;
    overflow: hidden;
    background: var(--white);
    box-shadow: 0 3px 8px rgba(0,0,0,0.18);
  }
  .card--light { top: 122px; }
  .card--dark { top: 676px; }
  .card__waves { position: absolute; inset: 0; width: 100%; height: 100%; }
  .brand {
    position: absolute;
    top: 46px;
    left: 0; right: 0;
    text-align: center;
    font-weight: 400;
    line-height: 1;
  }
  .brand__name { display: block; font-size: 50px; letter-spacing: 1px; }
  .brand__tag { display: block; font-size: 17px; letter-spacing: 11px; margin-top: 6px; padding-left: 11px; }
  .card--light .brand { color: var(--white); }
  .card--dark .brand { color: var(--blue); }

  .holder {
    position: absolute;
    top: 196px;
    left: 0; right: 0;
    text-align: center;
    font-size: 32px;
    font-weight: 400;
    line-height: 1;
  }
  .holder__first { font-weight: 700; }
  .card--light .holder__first { color: var(--blue); }
  .card--light .holder__rest { color: var(--green); }
  .card--dark .holder { color: var(--white); }

  .role {
    position: absolute;
    top: 240px;
    left: 0; right: 0;
    text-align: center;
    font-size: 19px;
  }
  .card--light .role { color: var(--ink); }
  .card--dark .role { color: var(--white); }

  .contacts {
    position: absolute;
    top: 290px;
    left: 0; right: 0;
    font-size: 19px;
    line-height: 27px;
  }
  .contacts__row { display: flex; justify-content: center; align-items: center; gap: 18px; white-space: nowrap; }
  .contact { display: inline-flex; align-items: center; gap: 5px; }
  .contact svg { width: 16px; height: 16px; flex: none; }
  .card--light .contacts { color: var(--ink); }
  .card--light .contact svg { fill: var(--green); }
  .card--dark .contacts { color: var(--white); }
  .card--dark .contact svg { fill: var(--white); }
</style>
</head>
<body>

<section class="card card--light">
  <svg class="card__waves" viewBox="0 0 857 488" preserveAspectRatio="none" aria-hidden="true">
    <path fill="var(--blue)" d="M0,0 H857 V30 C845,140 720,210 480,220 C300,225 130,190 0,150 Z"/>
    <path fill="var(--green)" d="M0,0 H818 C835,100 760,172 560,190 C380,206 150,182 0,132 Z"/>
  </svg>
  <div class="brand"><span class="brand__name">Pathbloom</span><span class="brand__tag">COUNSELING</span></div>
  <h1 class="holder"><span class="holder__first">Marcus T.</span> <span class="holder__rest">Whitfield, Ph.D.</span></h1>
  <p class="role">Licensed Clinical Psychologist/ Integrative Health Coach</p>
  <div class="contacts">
    <div class="contacts__row">
      <span class="contact"><svg viewBox="0 0 16 16"><rect width="16" height="16" rx="3"/><path fill="var(--white)" d="M5 3.5l1.6 2.3-1 1c.6 1.3 1.4 2.1 2.6 2.7l1-1 2.3 1.5-.7 2c-3.6-.2-6.6-3.1-6.8-6.8z"/></svg>(541) 555-0142</span>
      <span class="contact"><svg viewBox="0 0 16 16"><rect x="5" y="1" width="8" height="5"/><rect x="1" y="5" width="3" height="10" rx="1"/><rect x="5" y="6" width="10" height="9" rx="1"/></svg>(541) 555-0186</span>
      <span class="contact"><svg viewBox="0 0 16 16"><rect y="2" width="16" height="12" rx="3"/><path fill="none" stroke="var(--white)" stroke-width="1.6" d="M3 5l5 4 5-4"/></svg>drmarcuswhitfield@kelvora.com</span>
    </div>
    <div class="contacts__row">
      <span class="contact"><svg viewBox="0 0 16 16"><path d="M8 0a5.5 5.5 0 0 0-5.5 5.5C2.5 10 8 16 8 16s5.5-6 5.5-10.5A5.5 5.5 0 0 0 8 0zm0 8a2.5 2.5 0 1 1 0-5 2.5 2.5 0 0 1 0 5z"/></svg>4812 Ferndale Pkwy NW Suite 730 Alder Falls, OR 97412</span>
    </div>
    <div class="contacts__row">
      <span class="contact"><svg viewBox="0 0 16 16"><circle cx="8" cy="8" r="8"/><path fill="var(--white)" d="M4 4c2 0 3 1 2.5 2.5S4 8 5 10s-1 2-2 1A6 6 0 0 1 4 4zm5 1c2 .5 3 2 2.5 4S9 12 9 13.5c2.5-.3 4-2 4.3-4C13 7 11 5 9 5z"/></svg>www.pathbloomcounseling.com</span>
    </div>
  </div>
</section>

<section class="card card--dark">
  <svg class="card__waves" viewBox="0 0 857 488" preserveAspectRatio="none" aria-hidden="true">
    <path fill="var(--green)" d="M818,0 H857 V488 H0 V128 C150,172 350,195 500,192 C680,186 805,125 818,0 Z"/>
    <path fill="var(--blue)" d="M0,140 C150,185 350,208 520,209 C700,208 830,150 857,55 V488 H0 Z"/>
  </svg>
  <div class="brand"><span class="brand__name">Pathbloom</span><span class="brand__tag">COUNSELING</span></div>
  <h2 class="holder"><span class="holder__first">Marcus T.</span> <span class="holder__rest">Whitfield, Ph.D.</span></h2>
  <p class="role">Licensed Clinical Psychologist/ Integrative Health Coach</p>
  <div class="contacts">
    <div class="contacts__row">
      <span class="contact"><svg viewBox="0 0 16 16"><rect width="16" height="16" rx="3"/><path fill="var(--blue)" d="M5 3.5l1.6 2.3-1 1c.6 1.3 1.4 2.1 2.6 2.7l1-1 2.3 1.5-.7 2c-3.6-.2-6.6-3.1-6.8-6.8z"/></svg>(541) 555-0142</span>
      <span class="contact"><svg viewBox="0 0 16 16"><rect x="5" y="1" width="8" height="5"/><rect x="1" y="5" width="3" height="10" rx="1"/><rect x="5" y="6" width="10" height="9" rx="1"/></svg>(541) 555-0186</span>
      <span class="contact"><svg viewBox="0 0 16 16"><rect y="2" width="16" height="12" rx="3"/><path fill="none" stroke="var(--blue)" stroke-width="1.6" d="M3 5l5 4 5-4"/></svg>drmarcuswhitfield@kelvora.com</span>
    </div>
    <div class="contacts__row">
      <span class="contact"><svg viewBox="0 0 16 16"><path d="M8 0a5.5 5.5 0 0 0-5.5 5.5C2.5 10 8 16 8 16s5.5-6 5.5-10.5A5.5 5.5 0 0 0 8 0zm0 8a2.5 2.5 0 1 1 0-5 2.5 2.5 0 0 1 0 5z"/></svg>4812 Ferndale Pkwy NW Suite 730 Alder Falls, OR 97412</span>
    </div>
    <div class="contacts__row">
      <span class="contact"><svg viewBox="0 0 16 16"><circle cx="8" cy="8" r="8"/><path fill="var(--blue)" d="M4 4c2 0 3 1 2.5 2.5S4 8 5 10s-1 2-2 1A6 6 0 0 1 4 4zm5 1c2 .5 3 2 2.5 4S9 12 9 13.5c2.5-.3 4-2 4.3-4C13 7 11 5 9 5z"/></svg>www.pathbloomcounseling.com</span>
    </div>
  </div>
</section>

</body>
</html>
```